Neudesign Homepage für Computerfirma
Zielgruppe
Wir sind ein seit 12 Jahren lokal ansässiger EDV Dienstleister mit Verkauf von PC, Notebooks etc. mit eigener Reparaturwerkstätte, Handel mit Computerzubehör. Zielgruppe: Klein- bis mittelständige Unternehmen / Organisationen, sowie Privatpersonen aller Altersgruppen.
Aufgabenstellung
Neudesign unserer Homepage: www.brivolt.at
responsives Design unter Beibehaltung unserer Logos bzw. Schriften und Farben( Logo kann gerne dezent verändert werden, aber die Charakteristik und Wiedererkennung muss bleiben ), gerne auch mit Webprogrammierung (CMS) welche aber separat ausgeschrieben/verhandelt wird. Seite soll komplett in HTML werden, technisch am Stand der Zeit mit allen Features die eine moderne HP haben soll.
Slogan "...damit Ihr Computer macht was er soll " wurde bisher schon oft verwendet und sollte wenn möglich eventuell untergebracht werden, gerne animiert.
Im Anhang einige bisher verwendete Grafiken zur Orientierung was bisher schon in Verwendung ist / war. (Bei Bedarf kann mehr geliefert werden)
Das Design sollte Kompetenz, Seriosität, renommiertes Unternehmen vermitteln. Kein Onlineshop momentan geplant. Schwerpunkt Reparatur/Wartung/Dienstleistung mit Ziel der Neukundengewinnung und Info für bestehende Kunden.
Grunddesign der Startseite, bei Bedarf je nach Designvorschlag auch Unterseite / Kontaktformular gerne im Direktauftrag, bei gefallen.

```html
<!DOCTYPE html>
<html lang="de">
<head>
<meta charset="utf-8">
<title>Brivolt – Computersysteme</title>
<link href="https://fonts.googleapis.com/css2?family=Titillium+Web:ital,wght@0,300;0,400;0,600;0,700;1,300;1,400;1,600&family=Fira+Sans:wght@400;500&family=Roboto:wght@300;400&display=swap" rel="stylesheet">
<style>
:root{
  --green:#7ab833;
  --green-mid:#5aaa30;
  --green-dark:#3c9a35;
  --green-deep:#0c5f38;
  --ink:#1f1d1c;
  --grey-text:#6b6b6b;
  --grey-hero:#8c8b89;
  --line:#d8d8d8;
  --white:#fff;
}
*{box-sizing:border-box;margin:0;padding:0}
html,body{width:684px;height:1200px;overflow:hidden;background:var(--white)}
body{position:relative;font-family:"Roboto",sans-serif;color:var(--grey-text)}
.abs{position:absolute}

/* header */
.brand{left:99px;top:37px;font-family:"Titillium Web",sans-serif;font-weight:700;font-size:22px;letter-spacing:1px;color:#555;line-height:1}
.nav{top:48px;left:246px;font-family:"Titillium Web",sans-serif;font-size:7.8px;color:#777;letter-spacing:.3px}
.nav span{position:absolute;white-space:nowrap}
.header-line{left:0;top:62px;width:684px;height:1.5px;background:var(--green)}
.header-band{left:6px;top:68px;width:678px;height:20px;background:linear-gradient(#fff,#c9c9c9 85%,#e9e9e9)}

/* hero */
.hero{left:0;top:88px;width:684px;height:158px;background:var(--grey-hero);overflow:hidden}
.hero-shape{position:absolute;inset:0}
.hero-photo{position:absolute;left:126px;top:0;width:237px;height:158px;background:radial-gradient(circle at 50% 30%,#dfe8f0 0,#7e8a92 18%,#3a3836 45%,#262423 80%)}
.hero-copy{position:absolute;right:134px;text-align:right;font-family:"Titillium Web",sans-serif;font-style:italic;color:#fff;line-height:1;white-space:nowrap}
.hero-l1{top:50px;font-weight:300;font-size:14px;color:#e8e8e8}
.hero-l2{top:67px;font-weight:600;font-size:15px}
.hero-l3{top:84px;font-weight:600;font-size:25px}
.btn{background:linear-gradient(#8cc63f,#5aa52d);color:#fff;font-family:"Roboto",sans-serif;font-size:6.6px;display:flex;align-items:center;justify-content:center}
.hero-btn{position:absolute;left:483px;top:120px;width:67px;height:14px}
.hero-shadow{left:0;top:246px;width:684px;height:14px;background:linear-gradient(#d5d5d5,#fff)}

/* headings */
.h2{font-family:"Titillium Web",sans-serif;font-style:italic;font-weight:300;font-size:12.5px;color:#666;letter-spacing:.2px;white-space:nowrap}
.h2 b{font-weight:600;color:var(--green)}
.services-title{left:93px;top:270px}

/* service cards */
.services{left:116px;top:304px;width:461px;height:176px;display:flex;box-shadow:0 10px 14px -8px rgba(0,0,0,.25)}
.service-card{flex:1;display:flex;flex-direction:column;align-items:center;padding-top:14px;background:linear-gradient(90deg,var(--green-mid),#86bf35)}
.service-card:nth-child(even){background:linear-gradient(90deg,var(--green-dark),#7bb934)}
.service-icon{width:52px;height:52px;border-radius:50%;background:#fff;border:3.5px solid var(--green-deep);display:flex;align-items:center;justify-content:center}
.service-name{margin-top:12px;font-family:"Fira Sans",sans-serif;font-size:8.4px;line-height:10.5px;color:var(--green-deep);text-align:center}
.service-text{margin-top:5px;font-family:"Fira Sans",sans-serif;font-size:6.7px;line-height:8.4px;color:#fff;white-space:nowrap}

/* text block */
.about-title{left:95px;top:530px}
.about{left:90px;top:567px;font-size:7.6px;line-height:12.1px;color:#7a7a7a;white-space:nowrap}
.about p{margin-bottom:12.1px}

/* contact */
.contact-title{left:396px;top:530px}
.form-label{left:395px;font-size:8.4px;color:#555}
.form-label i{font-style:normal;color:var(--green)}
.field{left:449px;width:101px;height:17px;border:1px solid var(--line);background:#fbfbfb}
.field-msg{width:121px;height:55px}
.send-btn{left:448px;top:724px;width:67px;height:14px}

/* footer */
.footer-band{left:0;top:797px;width:684px;height:13px;background:linear-gradient(#fff,#cfcfcf)}
.footer{left:0;top:810px;width:684px;height:157px;background:var(--ink)}
.footer-col{position:absolute;top:17px;font-family:"Fira Sans",sans-serif;font-weight:500;font-size:8.4px;line-height:11px;color:#fff;white-space:nowrap}
</style>
</head>
<body>

<header>
  <div class="abs brand">BRIVOLT</div>
  <nav class="abs nav">
    <span style="left:0">BRIVOLT</span>
    <span style="left:51px">BRINEWS</span>
    <span style="left:106px">BRISERIE</span>
    <span style="left:161px">BRILINE</span>
    <span style="left:212px">SERVICE</span>
    <span style="left:259px">KONTAKT</span>
  </nav>
  <div class="abs header-band"></div>
  <div class="abs header-line"></div>
</header>

<section class="abs hero">
  <svg class="hero-shape" viewBox="0 0 684 158" preserveAspectRatio="none" aria-hidden="true">
    <polygon points="0,0 442,0 287,158 0,158" fill="#252322"/>
  </svg>
  <div class="hero-photo" role="img" aria-label="Foto: Mann vor einer Tafel mit Online-Marketing-Skizzen, Blick ins Licht"></div>
  <svg class="hero-shape" viewBox="0 0 684 158" preserveAspectRatio="none" aria-hidden="true">
    <polygon points="442,0 684,0 684,158 287,158" fill="#8c8b89"/>
  </svg>
  <div class="hero-copy hero-l1">DAMIT IHR</div>
  <div class="hero-copy hero-l2">COMPUTER MACHT</div>
  <div class="hero-copy hero-l3">WAS ER SOLL</div>
  <div class="btn hero-btn">Erfahren sie mehr</div>
</section>
<div class="abs hero-shadow"></div>

<h2 class="abs h2 services-title">MIT UNSEREM SERVICE <b>BLEIBT KEIN WUNSCH OFFEN!</b></h2>

<div class="abs services">
  <div class="service-card">
    <div class="service-icon"><svg width="24" height="22" viewBox="0 0 24 22" fill="#0c5f38"><rect x="1" y="14" width="4" height="8"/><rect x="7" y="10" width="4" height="12"/><rect x="13" y="6" width="4" height="16"/><rect x="19" y="2" width="4" height="20"/></svg></div>
    <div class="service-name">Kunden<br>Beratung</div>
    <div class="service-text">Lorem ipsum dolor sit<br>amet, consetetur<br>sadipscing elitr, sed<br>diam nonumy eirmod<br>tempor invidunt</div>
  </div>
  <div class="service-card">
    <div class="service-icon"><svg width="24" height="24" viewBox="0 0 24 24" fill="none" stroke="#0c5f38" stroke-width="2.5"><path d="M12 3l3 6 6 1-4.5 4.5 1 6.5-5.5-3-5.5 3 1-6.5L3 10l6-1z" fill="#0c5f38"/></svg></div>
    <div class="service-name">Geschwindigkeits<br>Test</div>
    <div class="service-text">Lorem ipsum dolor sit<br>amet, consetetur<br>sadipscing elitr, sed<br>diam nonumy eirmod<br>tempor invidunt</div>
  </div>
  <div class="service-card">
    <div class="service-icon"><svg width="24" height="24" viewBox="0 0 24 24" fill="none" stroke="#0c5f38" stroke-width="2.6"><circle cx="10" cy="10" r="7"/><path d="M15 15l7 7"/></svg></div>
    <div class="service-name">Aktive<br>Fehlersuche</div>
    <div class="service-text">Lorem ipsum dolor sit<br>amet, consetetur<br>sadipscing elitr, sed<br>diam nonumy eirmod<br>tempor invidunt</div>
  </div>
  <div class="service-card">
    <div class="service-icon"><svg width="24" height="22" viewBox="0 0 24 22" fill="none" stroke="#0c5f38" stroke-width="2.4"><path d="M14 4a5 5 0 0 0 6 6L10 20a2.5 2.5 0 0 1-4-4L16 6a5 5 0 0 1-2-2z" fill="#0c5f38"/></svg></div>
    <div class="service-name">Sofort<br>Reparatur</div>
    <div class="service-text">Lorem ipsum dolor sit<br>amet, consetetur<br>sadipscing elitr, sed<br>diam nonumy eirmod<br>tempor invidunt</div>
  </div>
  <div class="service-card">
    <div class="service-icon"><svg width="24" height="22" viewBox="0 0 24 22" fill="#0c5f38"><rect x="1" y="1" width="22" height="14" rx="1"/><rect x="3" y="3" width="18" height="10" fill="#fff"/><rect x="9" y="15" width="6" height="4"/><rect x="6" y="19" width="12" height="2"/></svg></div>
    <div class="service-name">Hardware<br>Bestellung</div>
    <div class="service-text">Lorem ipsum dolor sit<br>amet, consetetur<br>sadipscing elitr, sed<br>diam nonumy eirmod<br>tempor invidunt</div>
  </div>
</div>

<h2 class="abs h2 about-title"><b>ATTRAKTIVE DIENSTLEISTUNGEN</b> FÜR SIE</h2>
<div class="abs about">
  <p>Das Dienstleistungsangebot reicht von der Beratung über Installation<br>und Inbetriebnahme bis hin zur Schulung und späteren Betreuung<br>und Wartung. Der Kunde, als Partner für eine langanhaltende und<br>für beide Seiten zufriedenstellende Geschäftsbeziehung, steht<br>dabei im Mittelpunkt unserer Geschäftstätigkeit.</p>
  <p>Flexibilität und Zukunftsorientiertheit sind Merkmale, die Sie von<br>uns erwarten können. Kundenspezifische Anpassungen bzw. Erweiterungen<br>der Soft- oder Hardware werden auf Wunsch, nach vorheriger Prüfung<br>auf die Machbarkeit, für unsere Kunden von uns durchgeführt.</p>
  <p>Sie haben Fragen, wir die Antworten.</p>
</div>

<h2 class="abs h2 contact-title"><b>KONTAKTIEREN</b> SIE UNS</h2>
<div class="abs form-label" style="top:556px">Vorname:<i>*</i></div>
<div class="abs field" style="top:553px"></div>
<div class="abs form-label" style="top:582px">Nachname:<i>*</i></div>
<div class="abs field" style="top:579px"></div>
<div class="abs form-label" style="top:608px">Email:<i>*</i></div>
<div class="abs field" style="top:605px"></div>
<div class="abs form-label" style="top:635px">Betreff:<i>*</i></div>
<div class="abs field" style="top:632px"></div>
<div class="abs form-label" style="top:659px">Nachricht:<i>*</i></div>
<div class="abs field field-msg" style="top:660px"></div>
<div class="abs btn send-btn">Versenden</div>

<div class="abs footer-band"></div>
<footer class="abs footer">
  <div class="footer-col" style="left:112px">BRI - Volt<br>BRI - News<br>BRI - Serie<br>BRI - Premium<br>BRI - Line</div>
  <div class="footer-col" style="left:257px">Firma<br>Brivolt - Computersysteme<br>Lindenweg 14<br>A-6830 Talhofen<br><br>Telefon: 05521 / 48120<br>Fax: 05521 / 48120 - 21<br>UID Nr. ATU 12345678</div>
  <div class="footer-col" style="left:439px">E-Mail: office@brivolt.at<br><br>Notdienst: pc-notdienst@brivolt.at<br>Produktanfrage: kundendienst@brivolt.at<br>Service: service@brivolt.at</div>
</footer>

</body>
</html>
```